Tech Startup Needs Business Card Design

I am looking for an eye catching business card design for our new company, Torn Kite. We are a place for business owners and contractors to share their experiences with their customers and check their current customers. Our website, www.torn-kite.co, may be able to offer some guidance as to the design.

Industry/Entity Type

Business

Contact Information for Business Card

Owen Barthwick
888-417-3083
Owen@torn-kite.co
www.torn-kite.co

```html
<!DOCTYPE html>
<html lang="en">
<head>
<meta charset="utf-8">
<title>Torn Kite – Business Cards</title>
<link rel="stylesheet" href="https://fonts.googleapis.com/css2?family=Lato:wght@400;700&display=swap">
<style>
  :root {
    --backdrop: #e9e7e4;
    --card-dark: #2a2a2a;
    --card-white: #fbfbfa;
    --brand-red: #e23a3a;
    --brand-red-deep: #c92c2c;
    --ink: #1d1d1d;
    --ink-soft: #3a3a3a;
    --rule-grey: #4a4a4a;
  }
  * { margin: 0; padding: 0; box-sizing: border-box; }
  html, body {
    width: 1200px; height: 800px; overflow: hidden;
    background: var(--backdrop);
    font-family: "Lato", sans-serif;
  }
  .sheet {
    position: relative; width: 1200px; height: 800px;
  }
  .card {
    position: absolute;
    width: 520px; height: 297px;
    background: var(--card-dark);
    border-radius: 4px;
    overflow: hidden;
    box-shadow: 0 6px 18px rgba(0,0,0,.18);
  }
  .card__panel {
    position: absolute; left: 0; top: 0;
    width: 488px; height: 268px;
    background: var(--card-white);
  }
  .card--front { left: 50px; top: 252px; }
  .card--back { left: 630px; top: 252px; }

  /* front */
  .front__swoosh {
    position: absolute; left: 0; top: 0; width: 520px; height: 297px;
  }
  .front__name {
    position: absolute; left: 34px; top: 40px;
    font-size: 19px; font-weight: 400; letter-spacing: 1px;
    color: var(--ink); text-transform: uppercase;
  }
  .front__rule {
    position: absolute; left: 0; top: 72px; height: 2px; width: 250px;
    background: linear-gradient(to right, var(--rule-grey) 0 62%, var(--brand-red) 62% 100%);
  }
  .contact {
    position: absolute; left: 30px; list-style: none;
  }
  .contact__item {
    display: flex; align-items: center; gap: 10px;
    font-size: 12.5px; color: var(--ink-soft);
    height: 22px; margin-bottom: 12px;
  }
  .contact__icon {
    width: 20px; height: 20px;
    border: 1.4px solid var(--brand-red); border-radius: 2px;
    display: flex; align-items: center; justify-content: center;
  }
  .front__brand {
    position: absolute; left: 318px; top: 128px;
    display: flex; align-items: center; gap: 8px;
    font-size: 22px; font-weight: 700; color: var(--brand-red);
  }
  .brand__dot {
    width: 14px; height: 14px; border-radius: 50%;
    background: var(--brand-red);
  }

  /* back */
  .back__brand {
    position: absolute; left: 0; top: 0; width: 488px; height: 268px;
    display: flex; align-items: center; justify-content: center; gap: 14px;
    font-size: 52px; font-weight: 700; color: var(--ink);
  }
  .back__brand .brand__dot { width: 30px; height: 30px; }
</style>
</head>
<body>
<main class="sheet">

  <section class="card card--front" aria-label="Business card front">
    <div class="card__panel"></div>
    <svg class="front__swoosh" viewBox="0 0 520 297" aria-hidden="true">
      <defs>
        <linearGradient id="swooshFill" x1="0" y1="0" x2="1" y2="1">
          <stop offset="0" stop-color="#e84545"/>
          <stop offset="1" stop-color="#c92c2c"/>
        </linearGradient>
      </defs>
      <path d="M300 268 C 380 262, 450 220, 488 150 L 520 150 L 520 297 L 300 297 Z" fill="url(#swooshFill)"/>
      <path d="M300 268 C 380 262, 450 220, 488 150 L 488 268 Z" fill="#e23a3a"/>
    </svg>

    <h1 class="front__name">Owen Barthwick</h1>
    <div class="front__rule"></div>

    <ul class="contact" style="top:108px">
      <li class="contact__item">
        <span class="contact__icon">
          <svg width="12" height="12" viewBox="0 0 24 24" aria-hidden="true"><path d="M6.6 10.8a15 15 0 0 0 6.6 6.6l2.2-2.2a1 1 0 0 1 1-.25 11.4 11.4 0 0 0 3.6.57 1 1 0 0 1 1 1V20a1 1 0 0 1-1 1A17 17 0 0 1 3 4a1 1 0 0 1 1-1h3.5a1 1 0 0 1 1 1c0 1.25.2 2.45.57 3.57a1 1 0 0 1-.25 1z" fill="none" stroke="#e23a3a" stroke-width="2"/></svg>
        </span>
        888-417-3083
      </li>
      <li class="contact__item">
        <span class="contact__icon">
          <svg width="12" height="10" viewBox="0 0 24 18" aria-hidden="true"><rect x="1" y="1" width="22" height="16" fill="none" stroke="#e23a3a" stroke-width="2"/><path d="M1 1 L12 10 L23 1" fill="none" stroke="#e23a3a" stroke-width="2"/></svg>
        </span>
        Owen@torn-kite.co
      </li>
    </ul>

    <div class="front__brand"><span class="brand__dot"></span>Torn Kite</div>
  </section>

  <section class="card card--back" aria-label="Business card back">
    <div class="card__panel"></div>
    <div class="back__brand"><span class="brand__dot"></span>Torn Kite</div>
  </section>

</main>
</body>
</html>
```